Design business card for new business which advocates for elders in nursing homes or personal care h

New business for rights of the elderly residents who reside in personal care homes and or nursing homes. I am looking for a business card with logo of keystone for Pennsylvania and something in side the keystone that represents healthcare, advocates, something on that line; monitor care received and needs of resident. Chart audits, State Regulation compliance

Target Market(s)

Seniors no longer safe to live at home by themselves along with their kids

Industry/Entity Type

Business

Contact Information for Business Card

Keystone symbol to represent Pensylvaoa with some kind of symbol inside to represent advocate, seniors, or healthcare symbol

Font styles to use
Serif

Colors
33a6d7
85cae6
abd037

Requirements
Must have
• Lanternfield Elder Allies is our business name; our tag line is Path to Caring Comfort
Nice to have
• Nice logo

```html
<!DOCTYPE html>
<html lang="en">
<head>
<meta charset="utf-8">
<title>Lanternfield Elder Allies — Business Card</title>
<link href="https://fonts.googleapis.com/css2?family=Cinzel:wght@600&family=Tinos:ital@0;1&display=swap" rel="stylesheet">
<style>
  :root {
    --blue: #33a6d7;
    --blue-light: #85cae6;
    --green: #abd037;
    --white: #ffffff;
    --backdrop: #e9ecee;
    --name-font: "Cinzel", serif;
    --body-font: "Tinos", serif;
  }
  html, body {
    margin: 0;
    padding: 0;
    width: 1200px;
    height: 938px;
    overflow: hidden;
    background: var(--backdrop);
  }
  .card {
    position: absolute;
    left: 75px;
    top: 169px;
    width: 1050px;
    height: 600px;
    background: linear-gradient(180deg, #3fb0de 0%, var(--blue) 60%);
    overflow: hidden;
    box-shadow: 0 10px 30px rgba(0,0,0,0.18);
  }
  .card__header {
    position: absolute;
    left: 0; top: 0;
    width: 100%;
    height: 195px;
    background: var(--white);
  }
  .card__header-tail {
    position: absolute;
    left: 810px;
    top: 194px;
  }
  .brand-mark {
    position: absolute;
    left: 70px;
    top: 62px;
    width: 110px;
    height: 110px;
    border-radius: 50%;
    background: var(--blue);
  }
  .brand-name {
    position: absolute;
    left: 215px;
    top: 78px;
    margin: 0;
    font-family: var(--name-font);
    font-weight: 600;
    font-size: 42px;
    letter-spacing: 1px;
    color: var(--blue);
    white-space: nowrap;
  }
  .brand-tagline {
    position: absolute;
    left: 300px;
    top: 132px;
    margin: 0;
    font-family: var(--body-font);
    font-size: 36px;
    color: var(--green);
    white-space: nowrap;
  }
  .contact-list {
    position: absolute;
    left: 590px;
    top: 238px;
    margin: 0;
    padding: 0;
    list-style: none;
    font-family: var(--body-font);
    font-size: 26px;
    color: var(--white);
  }
  .contact-list li {
    display: flex;
    align-items: center;
    height: 50px;
  }
  .contact-list svg {
    width: 40px;
    height: 36px;
    margin-right: 22px;
    flex: none;
  }
  .address {
    position: absolute;
    left: 62px;
    top: 330px;
    font-family: var(--body-font);
    color: var(--white);
    font-style: normal;
  }
  .address__label {
    display: block;
    font-style: italic;
    font-size: 32px;
    margin-bottom: 8px;
  }
  .address__line {
    display: block;
    font-size: 24px;
    line-height: 30px;
  }
  .card__footer {
    position: absolute;
    left: 0;
    bottom: 0;
    width: 100%;
    height: 112px;
    background: var(--green);
  }
</style>
</head>
<body>
  <div class="card">
    <div class="card__header">
      <span class="brand-mark" aria-hidden="true"></span>
      <h1 class="brand-name">Lanternfield Elder Allies</h1>
      <p class="brand-tagline">Path to Caring Comfort</p>
    </div>
    <svg class="card__header-tail" width="110" height="50" viewBox="0 0 110 50" aria-hidden="true">
      <polygon points="0,0 110,0 110,0 65,48" fill="#ffffff"/>
    </svg>

    <ul class="contact-list">
      <li>
        <svg viewBox="0 0 40 36" aria-hidden="true">
          <path d="M4 2h28a4 4 0 0 1 4 4v18a4 4 0 0 1-4 4h-4l6 6-12-6H4a4 4 0 0 1-4-4V6a4 4 0 0 1 4-4z" fill="#ffffff"/>
          <path d="M12 8c1-1 3-1 3 1l1 3c0 1-1 2-2 2 1 3 3 5 6 6 0-1 1-2 2-2l3 1c2 0 2 2 1 3-2 2-5 2-9-1-3-3-5-6-5-9 0-2 0-3 0-4z" fill="var(--blue)"/>
        </svg>
        <span>+1.555.014-2287</span>
      </li>
      <li>
        <svg viewBox="0 0 40 36" aria-hidden="true">
          <path d="M4 2h28a4 4 0 0 1 4 4v18a4 4 0 0 1-4 4h-4l6 6-12-6H4a4 4 0 0 1-4-4V6a4 4 0 0 1 4-4z" fill="#ffffff"/>
          <rect x="8" y="8" width="20" height="13" fill="none" stroke="var(--blue)" stroke-width="2"/>
          <polyline points="8,8 18,16 28,8" fill="none" stroke="var(--blue)" stroke-width="2"/>
        </svg>
        <span>allies@lanternfield.com</span>
      </li>
      <li>
        <svg viewBox="0 0 40 36" aria-hidden="true">
          <path d="M4 2h28a4 4 0 0 1 4 4v18a4 4 0 0 1-4 4h-4l6 6-12-6H4a4 4 0 0 1-4-4V6a4 4 0 0 1 4-4z" fill="#ffffff"/>
          <circle cx="18" cy="15" r="8" fill="none" stroke="var(--blue)" stroke-width="2"/>
          <ellipse cx="18" cy="15" rx="3.5" ry="8" fill="none" stroke="var(--blue)" stroke-width="1.5"/>
          <line x1="10" y1="15" x2="26" y2="15" stroke="var(--blue)" stroke-width="1.5"/>
        </svg>
        <span>www.lanternfield.com</span>
      </li>
    </ul>

    <address class="address">
      <span class="address__label">Address :</span>
      <span class="address__line">412 – 90</span>
      <span class="address__line">Rue des Érables Est,</span>
      <span class="address__line">Montréal (Québec) H9Z 1K7 Canada</span>
    </address>

    <div class="card__footer"></div>
  </div>
</body>
</html>
```